Design some Business Cards for Gleaming Wheel Studio

I require some business cards to be design for my car detailing business "Gleaming Wheel Studio".

Preferred layout is landscape and artwork MUST be created in CMYK format and 300 dpi. Information that should be included is

Marcus Whitby
Vehicle Detailing Specialist

Tel: 07715 492 618
Email : marcus@gleamingwheelstudio.co.uk
Website : www.gleamingwheelstudio.co.uk

One side should have just the logo and maybe some design element - I have attached a example of a business card which I do like the black side with the image just visible behind the text (example.jpg). The other side should have all of the contact information and probably the logo on it too.

Plenty of images on my website if needed www.gleamingwheelstudio.co.uk

It should have a classy look to it and be very simple and stylish .

Please do not use any templates or clip art

```html
<!DOCTYPE html>
<html lang="en">
<head>
<meta charset="utf-8">
<title>Gleaming Wheel Studio – Business Cards</title>
<link rel="stylesheet" href="https://fonts.googleapis.com/css2?family=Open+Sans:wght@400;600;700&display=swap">
<style>
  :root {
    --backdrop: #e9e6e2;
    --card: #ffffff;
    --ink-black: #111111;
    --band-grey: #3c3c3c;
    --pale-disc: #f0f0f0;
    --accent-green: #7ac143;
    --logo-grey: #8a8a8a;
    --text-dark: #222222;
    --text-light: #e6e6e6;
  }
  html, body {
    margin: 0;
    width: 1200px;
    height: 912px;
    overflow: hidden;
    background: var(--backdrop);
    font-family: "Open Sans", Arial, sans-serif;
  }
  .sheet {
    position: relative;
    width: 1200px;
    height: 912px;
  }
  .card {
    position: absolute;
    left: 230px;
    width: 740px;
    height: 420px;
    background: var(--card);
    overflow: hidden;
    box-shadow: 0 6px 18px rgba(0,0,0,0.18);
  }
  .card--front { top: 24px; }
  .card--back { top: 468px; }
  .card__shapes {
    position: absolute;
    inset: 0;
    width: 100%;
    height: 100%;
  }
  .logo {
    position: absolute;
    top: 52px;
    right: 48px;
    display: flex;
    align-items: center;
    gap: 12px;
  }
  .logo__square {
    width: 30px;
    height: 30px;
    background: var(--accent-green);
  }
  .logo__name {
    font-size: 22px;
    font-weight: 600;
    letter-spacing: 1px;
    text-transform: uppercase;
    color: var(--logo-grey);
  }
  .person__name {
    position: absolute;
    right: 48px;
    top: 222px;
    margin: 0;
    font-size: 30px;
    font-weight: 700;
    line-height: 40px;
    color: var(--accent-green);
  }
  .band-text {
    position: absolute;
    right: 48px;
    top: 268px;
    margin: 0;
    font-size: 19px;
    line-height: 46px;
    color: var(--text-light);
    letter-spacing: 0.5px;
  }
  .contact {
    position: absolute;
    left: 40px;
    top: 146px;
    margin: 0;
    padding: 0;
    list-style: none;
    font-size: 15px;
    color: var(--text-dark);
    line-height: 32px;
  }
  .contact__item {
    display: flex;
    align-items: center;
    gap: 10px;
  }
  .contact__icon {
    width: 14px;
    height: 14px;
    flex: none;
  }
  .back-web {
    position: absolute;
    right: 48px;
    top: 268px;
    margin: 0;
    font-size: 19px;
    line-height: 46px;
    color: var(--text-light);
  }
</style>
</head>
<body>
<main class="sheet">

  <section class="card card--front" aria-label="Business card, contact side">
    <svg class="card__shapes" viewBox="0 0 740 420" aria-hidden="true">
      <circle cx="120" cy="540" r="470" fill="var(--pale-disc)"/>
      <path d="M0 0 H360 A300 300 0 0 0 200 130 H0 Z" fill="var(--ink-black)"/>
      <rect x="0" y="268" width="740" height="46" fill="var(--band-grey)"/>
    </svg>

    <div class="logo">
      <span class="logo__square"></span>
      <span class="logo__name">Gleaming Wheel Studio</span>
    </div>

    <ul class="contact">
      <li class="contact__item">
        <svg class="contact__icon" viewBox="0 0 14 14"><path d="M3 1h3l1 3-2 1a7 7 0 0 0 4 4l1-2 3 1v3a1 1 0 0 1-1 1A12 12 0 0 1 2 2a1 1 0 0 1 1-1z" fill="var(--text-dark)"/></svg>
        07715 492 618
      </li>
      <li class="contact__item">
        <svg class="contact__icon" viewBox="0 0 14 14"><rect x="1" y="3" width="12" height="8" fill="none" stroke="var(--text-dark)" stroke-width="1.4"/><path d="M1 3l6 5 6-5" fill="none" stroke="var(--text-dark)" stroke-width="1.4"/></svg>
        marcus@gleamingwheelstudio.co.uk
      </li>
      <li class="contact__item">
        <svg class="contact__icon" viewBox="0 0 14 14"><circle cx="7" cy="7" r="5.5" fill="none" stroke="var(--text-dark)" stroke-width="1.4"/><path d="M1.5 7h11M7 1.5c-3 3-3 8 0 11M7 1.5c3 3 3 8 0 11" fill="none" stroke="var(--text-dark)" stroke-width="1.2"/></svg>
        www.gleamingwheelstudio.co.uk
      </li>
    </ul>

    <h1 class="person__name">Marcus Whitby</h1>
    <p class="band-text">Vehicle Detailing Specialist</p>
  </section>

  <section class="card card--back" aria-label="Business card, logo side">
    <svg class="card__shapes" viewBox="0 0 740 420" aria-hidden="true">
      <circle cx="120" cy="540" r="470" fill="var(--pale-disc)"/>
      <path d="M0 0 H360 A300 300 0 0 0 200 130 H0 Z" fill="var(--ink-black)"/>
      <rect x="0" y="268" width="740" height="46" fill="var(--band-grey)"/>
    </svg>

    <div class="logo">
      <span class="logo__square"></span>
      <span class="logo__name">Gleaming Wheel Studio</span>
    </div>

    <p class="back-web">www.gleamingwheelstudio.co.uk</p>
  </section>

</main>
</body>
</html>
```